Tovimerra: Travel business card redesign

We need a clean elegant look for our cards featuring blue and orange. Look should communicate a sense of strong design and seem uncluttered. The company is Tovimerra which means escape to bliss. As in every trip is an escape to bliss. Feel free to reinvent the logo or just tweak it. Colors should be blue like Caribbean waters and a saturated orange. Keep it clean and simple.
Please match the information in the sample uploaded but the sample is horrible -- a non-starter -- use for information only. also please add managing director to my name as title

Target Market(s)
potential clients, hotels, trade publications
Industry/Entity Type
Travel Industry
Contact Information for Business Card
as above
Requirements
Must have
- Font should be century gothic. Colors below are close but a but prefer lighter in each case.

```html
<!DOCTYPE html>
<html lang="en">
<head>
<meta charset="utf-8">
<title>Tovimerra – Business Card</title>
<link rel="stylesheet" href="https://fonts.googleapis.com/css2?family=Questrial&display=swap">
<style>
  :root {
    --stage: #2b2b2d;
    --card-white: #ffffff;
    --card-black: #141416;
    --orange: #f0892a;
    --blue: #5aaad8;
    --ink: #555558;
    --rule: #b9b9bc;
  }
  * { box-sizing: border-box; margin: 0; padding: 0; }
  html, body {
    width: 1200px;
    height: 900px;
    overflow: hidden;
    background: var(--stage);
    font-family: "Questrial", "Century Gothic", sans-serif;
  }
  .stage {
    width: 1200px;
    height: 900px;
    display: flex;
    align-items: center;
    justify-content: center;
    gap: 40px;
  }
  .card {
    position: relative;
    width: 540px;
    height: 310px;
    border-radius: 22px;
    box-shadow: 0 10px 28px rgba(0,0,0,0.35);
  }
  .card--front { background: var(--card-white); }
  .card--back {
    background: var(--card-black);
    display: flex;
    align-items: center;
    justify-content: center;
  }
  .wordmark {
    color: var(--orange);
    font-weight: 400;
    letter-spacing: -1px;
    line-height: 1;
  }
  .card--front .wordmark {
    position: absolute;
    top: 48px;
    right: 34px;
    font-size: 62px;
  }
  .card--back .wordmark { font-size: 68px; }
  .divider {
    position: absolute;
    left: 196px;
    right: 30px;
    top: 146px;
    height: 1px;
    background: var(--rule);
  }
  .person {
    position: absolute;
    left: 32px;
    top: 132px;
  }
  .person__name {
    color: var(--orange);
    font-size: 20px;
    line-height: 1.1;
  }
  .person__title {
    color: var(--blue);
    font-size: 14px;
    margin-top: 2px;
  }
  .contacts {
    position: absolute;
    right: 30px;
    top: 160px;
    list-style: none;
    text-align: right;
    color: var(--ink);
    font-size: 13.5px;
  }
  .contacts li {
    display: flex;
    align-items: center;
    justify-content: flex-end;
    gap: 7px;
    height: 21px;
  }
  .contacts svg { width: 12px; height: 12px; flex: none; }
  .address {
    position: absolute;
    left: 32px;
    bottom: 42px;
    color: var(--ink);
    font-size: 15px;
    line-height: 1.4;
    font-style: normal;
  }
</style>
</head>
<body>
<main class="stage">
  <section class="card card--front">
    <div class="wordmark">tovimerra</div>
    <div class="divider"></div>
    <div class="person">
      <div class="person__name">Elan Varga</div>
      <div class="person__title">Managing Director</div>
    </div>
    <ul class="contacts">
      <li>877.55.TOVIM(868646)
        <svg viewBox="0 0 12 12" aria-hidden="true"><path d="M2.5 1 L4.5 1 L5.2 3.4 L4 4.4 Q5 6.8 7.6 8 L8.6 6.8 L11 7.5 L11 9.5 Q10.5 11 9 11 Q1 10 1 3 Q1 1.5 2.5 1 Z" fill="var(--orange)"/></svg>
      </li>
      <li>323.555.0148
        <svg viewBox="0 0 12 12" aria-hidden="true"><rect x="3" y="0.5" width="6" height="11" rx="1.2" fill="none" stroke="var(--orange)" stroke-width="1.4"/><circle cx="6" cy="9.6" r="0.8" fill="var(--orange)"/></svg>
      </li>
      <li>310.555.0192
        <svg viewBox="0 0 12 12" aria-hidden="true"><rect x="1" y="4.5" width="10" height="6.5" rx="1" fill="var(--orange)"/><rect x="3" y="1" width="6" height="4" fill="none" stroke="var(--orange)" stroke-width="1.2"/><rect x="3" y="6.5" width="6" height="1.2" fill="#fff"/></svg>
      </li>
      <li>www.tovimerra.com
        <svg viewBox="0 0 12 12" aria-hidden="true"><circle cx="6" cy="6" r="5.3" fill="var(--orange)"/><path d="M1 6 H11 M6 0.8 Q3 6 6 11.2 M6 0.8 Q9 6 6 11.2" fill="none" stroke="#fff" stroke-width="0.8"/></svg>
      </li>
    </ul>
    <address class="address">1460 Harbor Crest Way N,<br>Seaview, 90218</address>
  </section>

  <section class="card card--back">
    <div class="wordmark">tovimerra</div>
  </section>
</main>
</body>
</html>
```